Brume vodka

With the logo attached in the subsequent file, a business card that reflects a premium and organic vodka. On the first side, the company logo in large. The names must be included on the back of the card (Miguel Ángel Tomás Ferrandis with the number +34 655 271 389 and Pau Berenguer Casals and +34 677 314 920). The slogan "What binds us" and "Organic and permium vodka" in bold E-mail (brumevodka@mailfield.net); Website www.brumevodkaorg.net

```html
<!DOCTYPE html>
<html lang="en">
<head>
<meta charset="utf-8">
<title>Brume Vodka – Business Card</title>
<link href="https://fonts.googleapis.com/css2?family=Lato:wght@400;700&display=swap" rel="stylesheet">
<style>
  :root {
    --stage: #1f1f20;
    --ink-dark: #2a2a2b;
    --paper: #ffffff;
    --silver: #9a9a9c;
    --text-light: #f2f2f2;
    --text-dark: #2a2a2b;
  }
  * { margin: 0; padding: 0; box-sizing: border-box; }
  html, body {
    width: 1200px; height: 912px; overflow: hidden;
    background: var(--stage);
    font-family: "Lato", sans-serif;
  }
  .sheet {
    width: 1200px; height: 912px;
    display: flex; flex-direction: column;
    align-items: center; justify-content: center; gap: 36px;
  }
  .card {
    position: relative;
    width: 700px; height: 400px;
    overflow: hidden;
  }
  /* Front */
  .card--front { background: var(--ink-dark); }
  .brand {
    position: absolute;
    display: flex; align-items: center; gap: 16px;
    font-weight: 400;
    letter-spacing: 0.06em;
    text-transform: uppercase;
    white-space: nowrap;
    line-height: 1;
  }
  .brand__dot {
    width: 20px; height: 20px; border-radius: 50%;
    background: currentColor; flex: none;
  }
  .card--front .brand {
    left: 50%; top: 160px; transform: translateX(-50%);
    font-size: 60px; color: var(--text-light);
  }
  .card--front .site {
    position: absolute; left: 0; right: 0; top: 262px;
    text-align: center; color: var(--text-light);
    font-size: 20px; letter-spacing: 0.02em;
  }
  /* Back */
  .card--back { background: var(--paper); }
  .back-art { position: absolute; inset: 0; width: 100%; height: 100%; }
  .tagline {
    position: absolute; right: 40px; top: 30px;
    text-align: right; font-weight: 700; font-size: 15px;
    text-transform: uppercase; color: var(--text-dark); line-height: 1.35;
  }
  .card--back .brand {
    left: 40px; top: 118px;
    font-size: 36px; color: var(--silver);
  }
  .card--back .brand__dot { width: 14px; height: 14px; }
  .contacts {
    position: absolute; right: 40px; top: 192px;
    text-align: right; color: var(--text-light);
  }
  .person { margin-bottom: 16px; }
  .person__name { font-weight: 700; font-size: 20px; line-height: 1.2; white-space: nowrap; }
  .person__phone { font-size: 15px; margin-top: 4px; display: flex; justify-content: flex-end; align-items: center; gap: 8px; }
  .links {
    position: absolute; left: 40px; bottom: 26px;
    color: var(--text-light); font-size: 17px;
  }
  .links__row { display: flex; align-items: center; gap: 12px; margin-top: 6px; }
  .icon { width: 15px; height: 15px; flex: none; }
</style>
</head>
<body>
<main class="sheet">
  <section class="card card--front">
    <div class="brand"><span class="brand__dot"></span>Brume Vodka</div>
    <p class="site">www.brumevodkaorg.net</p>
  </section>

  <section class="card card--back">
    <svg class="back-art" viewBox="0 0 700 400" preserveAspectRatio="none">
      <path transform="translate(0,-24)" d="M0,300 C180,296 260,280 330,200 C400,120 480,100 700,98" fill="none" stroke="var(--silver)" stroke-width="14"/>
      <path transform="translate(0,-9)" d="M0,300 C180,296 260,280 330,200 C400,120 480,100 700,98" fill="none" stroke="var(--ink-dark)" stroke-width="3"/>
      <path d="M0,300 C180,296 260,280 330,200 C400,120 480,100 700,98 L700,400 L0,400 Z" fill="var(--ink-dark)"/>
    </svg>

    <p class="tagline">What binds us<br>Organic and permium vodka</p>

    <div class="brand"><span class="brand__dot"></span>Brume Vodka</div>

    <div class="contacts">
      <div class="person">
        <p class="person__name">Miguel Ángel Tomás Ferrandis</p>
        <p class="person__phone">
          <svg class="icon" viewBox="0 0 24 24"><path fill="currentColor" d="M6.6 10.8a15 15 0 0 0 6.6 6.6l2.2-2.2c.3-.3.7-.4 1-.2 1.1.4 2.3.6 3.6.6.6 0 1 .4 1 1V20c0 .6-.4 1-1 1A17 17 0 0 1 3 4c0-.6.4-1 1-1h3.5c.6 0 1 .4 1 1 0 1.3.2 2.5.6 3.6.1.3 0 .7-.2 1z"/></svg>
          +34 655 271 389
        </p>
      </div>
      <div class="person">
        <p class="person__name">Pau Berenguer Casals</p>
        <p class="person__phone">
          <svg class="icon" viewBox="0 0 24 24"><path fill="currentColor" d="M6.6 10.8a15 15 0 0 0 6.6 6.6l2.2-2.2c.3-.3.7-.4 1-.2 1.1.4 2.3.6 3.6.6.6 0 1 .4 1 1V20c0 .6-.4 1-1 1A17 17 0 0 1 3 4c0-.6.4-1 1-1h3.5c.6 0 1 .4 1 1 0 1.3.2 2.5.6 3.6.1.3 0 .7-.2 1z"/></svg>
          +34 677 314 920
        </p>
      </div>
    </div>

    <div class="links">
      <p class="links__row">
        <svg class="icon" viewBox="0 0 24 24"><path fill="currentColor" d="M2 5h20v14H2z"/><path fill="none" stroke="var(--ink-dark)" stroke-width="1.6" d="M2 5l10 8 10-8"/></svg>
        brumevodka@mailfield.net
      </p>
      <p class="links__row">
        <svg class="icon" viewBox="0 0 24 24"><circle cx="12" cy="12" r="10" fill="currentColor"/><path fill="none" stroke="var(--ink-dark)" stroke-width="1.4" d="M2 12h20M12 2c3 3 3 17 0 20M12 2c-3 3-3 17 0 20"/></svg>
        www.brumevodkaorg.net
      </p>
    </div>
  </section>
</main>
</body>
</html>
```